Finch Haulage Ltd

We need an A5 size (UK size) flyer to advertise our new business which is called Finch Haulage.
Domestic and Commercial Waste Clearance Services.
Please have the question in bold "Do you have a pile of junk you need to dispose of?"
We collect all kinds of junk or rubbish from homes and businesses across Kent, Sussex and South London.
No fuss, no mess!
A low cost, hassle free alternative to skip hire.
Licensed by the Landcare Board and fully insured (this can be in small print at the bottom).
Please put the Recycle symbol somewhere.
Our tagline on our vehicle is "We Clear More, For Less!"
We'd like the flyer to be bold and eye-catching (to catch the eye of the homeowner or business owner while it's sitting on their doormat).
We need our telephone, website and email to be prominent. Maybe saying "Call today for a free quote"
Tel. 01734 586019
Email: info@finchhaulage.example.co.uk
www.finchhaulage.example.co.uk
Target Market(s)
Our market will be homes and small businesses around Kent, Sussex and South London.

```html
<!DOCTYPE html>
<html lang="en">
<head>
<meta charset="utf-8">
<title>Finch Haulage – Waste Clearance Flyer</title>
<link rel="stylesheet" href="https://fonts.googleapis.com/css2?family=Roboto+Condensed:ital,wght@0,400;0,500;0,700;1,700&family=Rubik:wght@600&display=swap">
<style>
  :root {
    --brand-green: #22b04b;
    --ink-grey: #4a4a4c;
    --soft-grey: #d6d7d9;
    --pale-grey: #eeeeef;
    --paper: #ffffff;
    --white: #ffffff;
  }
  * { margin: 0; padding: 0; box-sizing: border-box; }
  html, body { width: 1200px; height: 866px; overflow: hidden; background: var(--paper); }
  .flyer {
    position: relative;
    width: 1200px;
    height: 866px;
    overflow: hidden;
    background: var(--paper);
    font-family: "Roboto Condensed", "Arial Narrow", sans-serif;
  }
  .backdrop { position: absolute; inset: 0; }

  .contact-phone {
    position: absolute; left: 44px; top: 22px;
    display: flex; align-items: center; gap: 14px;
    color: var(--white); font-weight: 500; font-size: 34px; letter-spacing: 1.5px;
  }
  .contact-email {
    position: absolute; right: 68px; top: 26px;
    display: flex; align-items: center; gap: 16px;
    color: var(--ink-grey); font-weight: 500; font-size: 27px; letter-spacing: 1.5px;
    text-transform: uppercase;
  }

  .brand-name {
    position: absolute; left: 60px; top: 226px; width: 440px;
    font-family: "Rubik", sans-serif; font-weight: 600;
    font-size: 58px; line-height: 1.05; letter-spacing: 4px;
    color: var(--ink-grey); text-transform: uppercase; text-align: center;
  }

  .headline {
    position: absolute; right: 28px; top: 196px;
    text-align: right; color: var(--brand-green);
    font-weight: 700; font-style: italic; font-size: 43px; line-height: 1.3;
    text-transform: uppercase; letter-spacing: 0.5px;
  }

  .service-copy {
    position: absolute; left: 562px; top: 346px; width: 620px;
    text-align: center; color: var(--ink-grey);
    font-family: "Rubik", sans-serif; font-weight: 600;
    font-size: 20px; line-height: 37px; letter-spacing: 0.8px;
    text-transform: uppercase;
  }

  .junk-photo {
    position: absolute; left: 70px; top: 440px; width: 480px; height: 330px;
    border-radius: 46% 52% 18% 20% / 40% 44% 14% 16%;
    background: radial-gradient(ellipse at 45% 55%, #c9c2a8 0%, #b8ad86 30%, #d7d3c8 62%, rgba(255,255,255,0) 78%);
  }

  .recycle-mark { position: absolute; left: 790px; top: 572px; width: 176px; height: 176px; }

  .footer-web {
    position: absolute; left: 42px; top: 786px;
    display: flex; align-items: center; gap: 12px;
    color: var(--ink-grey); font-weight: 500; font-size: 27px;
  }
  .footer-licence {
    position: absolute; left: 42px; top: 828px;
    color: var(--ink-grey); font-weight: 400; font-size: 21px;
  }
</style>
</head>
<body>
<main class="flyer">
  <svg class="backdrop" width="1200" height="866" viewBox="0 0 1200 866" aria-hidden="true">
    <defs>
      <linearGradient id="greyBand" x1="0" y1="0" x2="1" y2="0">
        <stop offset="0" stop-color="#f3f3f4"/>
        <stop offset="1" stop-color="#cfd0d2"/>
      </linearGradient>
    </defs>
    <path d="M0,0 H1200 V120 C1080,104 980,178 860,160 C760,145 690,120 560,138 C430,156 300,150 200,146 L0,140 Z" fill="url(#greyBand)"/>
    <path d="M0,0 H650 C610,70 560,100 470,112 C330,128 160,112 60,150 C30,162 12,176 0,190 Z" fill="var(--brand-green)"/>
    <path d="M0,380 C20,520 70,650 180,740 C250,790 330,810 420,820 L0,866 Z" fill="url(#greyBand)"/>
    <path d="M0,380 C20,520 70,650 180,740" fill="none" stroke="var(--brand-green)" stroke-width="8"/>
    <path d="M0,760 C200,800 420,815 700,808 C900,802 1060,790 1200,776 V866 H0 Z" fill="url(#greyBand)"/>
    <path d="M480,800 C720,804 960,790 1200,760 V866 H1080 C920,834 700,808 480,800 Z" fill="var(--brand-green)"/>
  </svg>

  <div class="contact-phone">
    <svg width="38" height="38" viewBox="0 0 38 38" aria-hidden="true">
      <circle cx="19" cy="19" r="16.5" fill="none" stroke="var(--white)" stroke-width="2.5"/>
      <path d="M14,10 l4,0 l1,5 l-2.5,1.8 c1,2.4 2.6,4.2 4.8,5.4 l1.9,-2.4 l5,1.2 l0,4 c-8,1.2 -15,-6 -14.2,-15 z" fill="var(--white)"/>
    </svg>
    <span>01734 586019</span>
  </div>

  <div class="contact-email">
    <svg width="36" height="24" viewBox="0 0 36 24" aria-hidden="true">
      <rect x="0" y="0" width="36" height="24" fill="var(--ink-grey)"/>
      <path d="M1,1 L18,14 L35,1" fill="none" stroke="var(--pale-grey)" stroke-width="2.5"/>
    </svg>
    <span>info@finchhaulage.example.co.uk</span>
  </div>

  <div class="brand-name">Finch Haulage</div>

  <h1 class="headline">Do you have a pile of junk<br>you need to dispose of?</h1>

  <p class="service-copy">We provide domestic and commercial waste clearance services across Kent, Sussex and South London. We collect all kinds of junk or rubbish from homes and business. No fuss, no mess! Very competitive prices.</p>

  <div class="junk-photo" role="img" aria-label="Photograph of a heap of household junk: tins, plastic bottles, bags and foil"></div>

  <svg class="recycle-mark" viewBox="-100 -100 200 200" role="img" aria-label="Recycle symbol">
    <g fill="var(--brand-green)">
      <path id="recycleArrow" d="M-20,-82 L20,-82 L52,-26 L68,-35 L60,16 L18,-2 L34,-11 L4,-62 L-8,-44 L-34,-58 Z"/>
      <use href="#recycleArrow" transform="rotate(120)"/>
      <use href="#recycleArrow" transform="rotate(240)"/>
    </g>
  </svg>

  <div class="footer-web">
    <svg width="22" height="22" viewBox="0 0 22 22" aria-hidden="true">
      <g fill="none" stroke="var(--ink-grey)" stroke-width="1.8">
        <circle cx="11" cy="11" r="9.5"/>
        <ellipse cx="11" cy="11" rx="4.2" ry="9.5"/>
        <path d="M1.5,11 H20.5 M3,6 H19 M3,16 H19"/>
      </g>
    </svg>
    <span>www.finchhaulage.example.co.uk</span>
  </div>
  <p class="footer-licence">Licensed by the Landcare Board and fully insured</p>
</main>
</body>
</html>
```